3 images for 3 products

Hopefully, nice and easy project.

New website under construction - www.deskvigor.co.uk selling a new type of office chair

The home page has a space for a large (674*327) gallery slider containing 3 images which will rotate in a loop. In that space I would like to put something relevant to the products (the 3 products are shown in the 3 boxes just below the large white space). At the moment, as you can see there is a large void which needs to be filled and all attempts that I have tried so far have been very amateurish

***Update***
Nice entry. Its not-animated banner and banner is probably the wrong word for this although is is the category that seemed to best fit.
I updated the site last night and if you have a look at the site at the moment its the main image(s) that needs to be replaced. Currently the slider is showing 2 images ("Modrun Pottery" and "Elegent Tapestry") These are the ones that need replacing with the 3 images
***********

The product then, is a type of seating that promotes good posture and activity as you are sitting on a ball on wheels that requires core stability muscles to be engaged

Here's how similar sites sell these chairs:-
http://www.pivotrumseat.com
http://www.torvexa.com/product/exercise-ball-wobblorb-chair.do
http://www.spineward.co.uk/perchly?gclid=CNrtlMbWzKkCFYpA4QodizANMg
spineward.com

If you need to understand a bit more about the chairs it's here as I have them for sale on Marketnook:-
http://www.marketnook.co.uk/Desk-Vigor-Exercise-Chair-Black/dp/X7731KQ2ZP/ref=sr_1_1?ie=UTF8&qid=1308854474&sr=8-1

The things that are fixed which I guess you will need to work with are:-
* the colours of the deskvigor logo
* the size of the space (674*327)
* possibly the colours that you already see on the site

Things which I guess I need to see although keeping an open mind are:-
* the 3 products in rotation

Other than that it's fairly free for you to work your magic

Thanks
Derek
Updates

A good example of how the 3 image slider works is here:-

http://www.thornwickstudio.com/

A further point I should have mentioned is that although the contest is due to run until July 3, I will probably be ending it before that date as I need to fill the blank space as the products are now live on Marketnook

Not sure if this helps but keywords that describe the product are:-
stability ball chair
posture ball chair
Desk Vigor
active seating

Target Market(s)

Adults 20-60, typically office workers

Industry/Entity Type

Construction

Requirements
Must have
• Images of balls

```html
<!DOCTYPE html>
<html lang="en">
<head>
<meta charset="utf-8">
<title>Desk Vigor – Ball Chair Slides</title>
<link rel="stylesheet" href="https://fonts.googleapis.com/css2?family=Anton&family=Arimo:wght@700&display=swap">
<style>
  :root {
    --page: #ffffff;
    --red-light: #d0282a;
    --red-mid: #bd1d1f;
    --red-dark: #9a1317;
    --orange-light: #fbae45;
    --orange-dark: #ef8519;
    --headline: #f6f6f6;
    --headline-shade: #2a0505;
    --label-text: #111111;
    --chair-light: #6a6a6a;
    --chair-dark: #2b2b2b;
  }
  * { margin: 0; padding: 0; box-sizing: border-box; }
  html, body {
    width: 1200px; height: 1200px; overflow: hidden;
    background: var(--page);
  }
  .slides { position: relative; width: 1200px; height: 1200px; }
  .slide {
    position: absolute; left: 207px; width: 786px; height: 378px; overflow: hidden;
    background:
      radial-gradient(ellipse at 55% 40%, var(--red-light) 0%, var(--red-mid) 55%, var(--red-dark) 100%);
  }
  .slide--active { top: 15px; }
  .slide--shock { top: 410px; }
  .slide--posture { top: 807px; }
  .headline {
    position: absolute; right: 22px; text-align: right; z-index: 2;
    font-family: "Anton", Impact, sans-serif; font-weight: 400;
    color: var(--headline); line-height: 1;
    letter-spacing: 6px; word-spacing: 12px;
    text-shadow: 2px 3px 3px var(--headline-shade);
    white-space: nowrap;
  }
  .headline span { display: block; }
  .slide--active .headline, .slide--shock .headline { top: 24px; font-size: 42px; }
  .slide--active .headline span + span,
  .slide--shock .headline span + span { margin-top: 28px; }
  .slide--posture .headline { top: 20px; font-size: 39px; letter-spacing: 5px; word-spacing: 10px; }
  .slide--posture .headline span + span { margin-top: 22px; }
  .chair {
    position: absolute; z-index: 1;
    background: radial-gradient(ellipse at 40% 35%, var(--chair-light) 0%, var(--chair-dark) 70%);
    border-radius: 12px;
  }
  .slide--active .chair { left: 63px; top: 82px; width: 233px; height: 288px; }
  .slide--shock .chair { left: 15px; top: 100px; width: 246px; height: 255px; }
  .slide--posture .chair { left: 15px; top: 18px; width: 218px; height: 350px; }
  .label {
    position: absolute; right: 0; z-index: 2;
    display: flex; align-items: center; justify-content: center;
    background: linear-gradient(to bottom, var(--orange-light), var(--orange-dark));
    box-shadow: -2px 3px 6px rgba(0,0,0,0.35);
    font-family: "Arimo", Arial, sans-serif; font-weight: 700;
    color: var(--label-text); white-space: nowrap;
  }
  .slide--active .label { left: 328px; top: 220px; height: 80px; font-size: 21px; }
  .slide--shock .label { left: 276px; top: 223px; height: 80px; font-size: 22px; }
  .slide--posture .label { left: 280px; top: 240px; height: 60px; font-size: 17px; }
</style>
</head>
<body>
<main class="slides">
  <section class="slide slide--active">
    <h2 class="headline"><span>A GREAT WAY TO STAY ACTIVE</span><span>WHILST SITTING</span></h2>
    <div class="chair" role="img" aria-label="Black exercise ball chair on a wheeled base"></div>
    <p class="label">Desk Vigor Exercise Ball Chair</p>
  </section>
  <section class="slide slide--shock">
    <h2 class="headline"><span>ACT AS A SHOCK ABSORBER</span><span>FOR THE SPINE</span></h2>
    <div class="chair" role="img" aria-label="Black exercise ball chair with a fixed backrest on a wheeled base"></div>
    <p class="label">Desk Vigor Ball Chair with Backrest</p>
  </section>
  <section class="slide slide--posture">
    <h2 class="headline"><span>IMPROVE POSTURE</span><span>ALLEVIATE BACK PAIN</span><span>IMPROVE CORE STRENGTH</span></h2>
    <div class="chair" role="img" aria-label="Grey exercise ball chair with an adjustable backrest on a wheeled base"></div>
    <p class="label">Desk Vigor Ball Chair with Adjustable - backrest</p>
  </section>
</main>
</body>
</html>
```